Banner Ad Design Project

I need a banner design for a new application which is going to the displayed on the TradeBazaar.

The banner is needed for this application:
https://portal.brivanta-cloud.example/tradebazaar/entryView?entryRef=k7Q84000002mxpdBRT

Example banners can be found here:
https://portal.brivanta-cloud.example/tradebazaar/entryView?entryRef=k7Q84000006hzswBRT

Or
https://portal.brivanta-cloud.example/tradebazaar/entryView?entryRef=k7Q84000002wLMRBR5

Target Market(s)

Enterprise business.

Requirements
Must have
• Must include our pendrowix logo.

```html
<!DOCTYPE html>
<html lang="en">
<head>
<meta charset="utf-8">
<title>Pendrowix – Approval History Reporting banners</title>
<link rel="stylesheet" href="https://fonts.googleapis.com/css2?family=Arimo:wght@400;700&display=swap">
<style>
  :root {
    --page-bg: #ffffff;
    --frame: #1a1a1a;
    --panel-white: #ffffff;
    --panel-grey-light: #f2f2f2;
    --panel-grey: #dcdcdc;
    --tagline: #444444;
    --brand-name: #f59a3c;
    --brand-dot: #4a7fc1;
    --photo-light: #f5f5f5;
    --photo-warm: #ebe7e3;
    --accent-blue: #3f6aa3;
    --accent-magenta: #b5509f;
    --accent-green: #6cbb3f;
    --accent-orange: #f5851f;
  }
  * { margin: 0; padding: 0; box-sizing: border-box; }
  html, body {
    width: 1200px; height: 800px; overflow: hidden;
    background: var(--page-bg);
    font-family: "Arimo", Arial, sans-serif;
  }
  .canvas { position: relative; width: 1200px; height: 800px; }
  .banner {
    position: absolute; left: 137px; width: 930px; height: 80px;
    border: 1px solid var(--frame);
    overflow: hidden;
    background: linear-gradient(90deg, var(--panel-grey) 20%, var(--panel-grey-light) 60%, var(--panel-white) 100%);
  }
  .banner--blue { top: 102px; --accent: var(--accent-blue); }
  .banner--magenta { top: 269px; --accent: var(--accent-magenta); }
  .banner--green { top: 447px; --accent: var(--accent-green); }
  .banner--orange { top: 617px; --accent: var(--accent-orange); }

  .banner__cloud { position: absolute; left: 0; top: 0; width: 240px; height: 80px; }
  .brand {
    position: absolute; left: 18px; top: 0; height: 80px;
    display: flex; align-items: center; gap: 36px;
  }
  .brand__dot { width: 40px; height: 40px; border-radius: 50%; background: var(--brand-dot); }
  .brand__name { font-size: 17px; font-weight: 400; color: var(--brand-name); }

  .banner__photo {
    position: absolute; right: 0; top: 0; width: 240px; height: 80px;
    background: linear-gradient(90deg, rgba(245,245,245,0) 0%, var(--photo-light) 35%, var(--photo-warm) 100%);
  }

  .headline {
    position: absolute; left: 230px; width: 505px; top: 1px;
    text-align: center;
    font-size: 38px; font-weight: 400; letter-spacing: 0.9px;
    color: var(--accent);
    white-space: nowrap;
  }
  .tagline {
    position: absolute; left: 230px; width: 495px; top: 49px;
    display: flex; justify-content: center; align-items: center; gap: 7px;
    font-size: 21px; font-weight: 700; color: var(--tagline);
    white-space: nowrap;
  }
  .tagline__sep { width: 18px; height: 18px; }
</style>
</head>
<body>
<div class="canvas">

  <section class="banner banner--blue">
    <svg class="banner__cloud" viewBox="0 0 240 80" aria-hidden="true">
      <path d="M0 0 H222 q-12 4 -10 12 q-14 4 -8 16 q-12 10 -4 22 q-6 14 8 20 q-4 8 4 10 H0 Z" fill="#000" opacity="0.18" transform="translate(4 0)"/>
      <path d="M0 0 H222 q-12 4 -10 12 q-14 4 -8 16 q-12 10 -4 22 q-6 14 8 20 q-4 8 4 10 H0 Z" fill="#fff"/>
    </svg>
    <div class="brand"><span class="brand__dot"></span><span class="brand__name">Pendrowix</span></div>
    <div class="banner__photo" role="img" aria-label="Photo of a hand touching a tablet screen"></div>
    <h1 class="headline">Approval History Reporting</h1>
    <p class="tagline">Monitoring
      <svg class="tagline__sep" viewBox="0 0 18 18" aria-hidden="true"><path d="M9 1 L17 5 V13 L9 17 L1 13 V5 Z" fill="#444"/><path d="M1 5 L9 9 L17 5 M9 9 V17" stroke="#fff" stroke-width="1.2" fill="none"/></svg>
      Tracking
      <svg class="tagline__sep" viewBox="0 0 18 18" aria-hidden="true"><path d="M9 1 L17 5 V13 L9 17 L1 13 V5 Z" fill="#444"/><path d="M1 5 L9 9 L17 5 M9 9 V17" stroke="#fff" stroke-width="1.2" fill="none"/></svg>
      Approving</p>
  </section>

  <section class="banner banner--magenta">
    <svg class="banner__cloud" viewBox="0 0 240 80" aria-hidden="true">
      <path d="M0 0 H222 q-12 4 -10 12 q-14 4 -8 16 q-12 10 -4 22 q-6 14 8 20 q-4 8 4 10 H0 Z" fill="#000" opacity="0.18" transform="translate(4 0)"/>
      <path d="M0 0 H222 q-12 4 -10 12 q-14 4 -8 16 q-12 10 -4 22 q-6 14 8 20 q-4 8 4 10 H0 Z" fill="#fff"/>
    </svg>
    <div class="brand"><span class="brand__dot"></span><span class="brand__name">Pendrowix</span></div>
    <div class="banner__photo" role="img" aria-label="Photo of a hand touching a tablet screen"></div>
    <h1 class="headline">Approval History Reporting</h1>
    <p class="tagline">Monitoring
      <svg class="tagline__sep" viewBox="0 0 18 18" aria-hidden="true"><path d="M9 1 L17 5 V13 L9 17 L1 13 V5 Z" fill="#444"/><path d="M1 5 L9 9 L17 5 M9 9 V17" stroke="#fff" stroke-width="1.2" fill="none"/></svg>
      Tracking
      <svg class="tagline__sep" viewBox="0 0 18 18" aria-hidden="true"><path d="M9 1 L17 5 V13 L9 17 L1 13 V5 Z" fill="#444"/><path d="M1 5 L9 9 L17 5 M9 9 V17" stroke="#fff" stroke-width="1.2" fill="none"/></svg>
      Approving</p>
  </section>

  <section class="banner banner--green">
    <svg class="banner__cloud" viewBox="0 0 240 80" aria-hidden="true">
      <path d="M0 0 H222 q-12 4 -10 12 q-14 4 -8 16 q-12 10 -4 22 q-6 14 8 20 q-4 8 4 10 H0 Z" fill="#000" opacity="0.18" transform="translate(4 0)"/>
      <path d="M0 0 H222 q-12 4 -10 12 q-14 4 -8 16 q-12 10 -4 22 q-6 14 8 20 q-4 8 4 10 H0 Z" fill="#fff"/>
    </svg>
    <div class="brand"><span class="brand__dot"></span><span class="brand__name">Pendrowix</span></div>
    <div class="banner__photo" role="img" aria-label="Photo of a hand touching a tablet screen"></div>
    <h1 class="headline">Approval History Reporting</h1>
    <p class="tagline">Monitoring
      <svg class="tagline__sep" viewBox="0 0 18 18" aria-hidden="true"><path d="M9 1 L17 5 V13 L9 17 L1 13 V5 Z" fill="#444"/><path d="M1 5 L9 9 L17 5 M9 9 V17" stroke="#fff" stroke-width="1.2" fill="none"/></svg>
      Tracking
      <svg class="tagline__sep" viewBox="0 0 18 18" aria-hidden="true"><path d="M9 1 L17 5 V13 L9 17 L1 13 V5 Z" fill="#444"/><path d="M1 5 L9 9 L17 5 M9 9 V17" stroke="#fff" stroke-width="1.2" fill="none"/></svg>
      Approving</p>
  </section>

  <section class="banner banner--orange">
    <svg class="banner__cloud" viewBox="0 0 240 80" aria-hidden="true">
      <path d="M0 0 H222 q-12 4 -10 12 q-14 4 -8 16 q-12 10 -4 22 q-6 14 8 20 q-4 8 4 10 H0 Z" fill="#000" opacity="0.18" transform="translate(4 0)"/>
      <path d="M0 0 H222 q-12 4 -10 12 q-14 4 -8 16 q-12 10 -4 22 q-6 14 8 20 q-4 8 4 10 H0 Z" fill="#fff"/>
    </svg>
    <div class="brand"><span class="brand__dot"></span><span class="brand__name">Pendrowix</span></div>
    <div class="banner__photo" role="img" aria-label="Photo of a hand touching a tablet screen"></div>
    <h1 class="headline">Approval History Reporting</h1>
    <p class="tagline">Monitoring
      <svg class="tagline__sep" viewBox="0 0 18 18" aria-hidden="true"><path d="M9 1 L17 5 V13 L9 17 L1 13 V5 Z" fill="#444"/><path d="M1 5 L9 9 L17 5 M9 9 V17" stroke="#fff" stroke-width="1.2" fill="none"/></svg>
      Tracking
      <svg class="tagline__sep" viewBox="0 0 18 18" aria-hidden="true"><path d="M9 1 L17 5 V13 L9 17 L1 13 V5 Z" fill="#444"/><path d="M1 5 L9 9 L17 5 M9 9 V17" stroke="#fff" stroke-width="1.2" fill="none"/></svg>
      Approving</p>
  </section>

</div>
</body>
</html>
```